Postcard Design

Little Plume is a boutique selling childrens toys and clothing. We have a lot of well known kids fashion labels such as Tavel K, Brindle, Zorra, Pebble Creek Sandals, Rovandi Kids and many more.
Save 10% when you shop online at www.littleplume.com.au. Use the code 10promo at the check out.
47 Harlow Lane, East Gosford NSW 2250 ph 02 45817362

Industry/Entity Type

Boutique

```html
<!DOCTYPE html>
<html lang="en">
<head>
<meta charset="utf-8">
<title>Little Plume – Save 10% Postcard</title>
<link rel="stylesheet" href="https://fonts.googleapis.com/css2?family=Rye&family=Indie+Flower&family=Arimo:wght@700&display=swap">
<style>
  :root {
    --peach: #f8d49c;
    --sky: #9fcfd7;
    --grass: #93bf5c;
    --blush: #f2a7a0;
    --purple: #4f2a8c;
    --white: #ffffff;
    --teal: #3fb7c7;
    --charcoal: #3d3d3d;
    --cherry: #d7343f;
    --balloon: #e8e0d4;
    --illus: #f4f4f0;
  }
  * { margin: 0; padding: 0; box-sizing: border-box; }
  html, body { width: 1200px; height: 929px; overflow: hidden; background: var(--white); }
  .postcard { position: relative; width: 1200px; height: 929px; overflow: hidden; background: var(--peach); }
  .bands, .type-layer { position: absolute; inset: 0; }
  .band-sky { fill: var(--sky); }
  .band-grass { fill: var(--grass); }
  .band-blush { fill: var(--blush); }
  .illustration { position: absolute; border-radius: 12px; opacity: .9; }
  .illustration.balloon { background: linear-gradient(180deg, var(--illus), var(--balloon)); border-radius: 50% 50% 40% 40%; }
  .illustration.ferris-wheel { background: var(--illus); border-radius: 50% 50% 8px 8px; opacity: .75; }
  .illustration.line-art { background: rgba(255,255,255,.55); }
  .headline { font-family: "Rye", serif; fill: var(--purple); }
  .script { font-family: "Indie Flower", cursive; fill: var(--white); }
  .web-address { font-family: "Arimo", sans-serif; font-weight: 700; fill: var(--white); }
  .promo-code { font-family: "Arimo", sans-serif; font-weight: 700; fill: var(--teal); }
  .labels { font-family: "Rye", serif; font-size: 22px; }
  .labels .light { fill: var(--white); }
  .labels .dark { fill: var(--charcoal); }
  .brand-dot { fill: var(--cherry); }
  .brand-name { font-family: "Rye", serif; fill: var(--purple); }
</style>
</head>
<body>
<main class="postcard">
  <div class="illustration balloon" style="left:0;top:0;width:115px;height:258px" role="img" aria-label="Striped hot air balloon"></div>
  <div class="illustration balloon" style="left:532px;top:0;width:130px;height:258px" role="img" aria-label="Striped hot air balloon"></div>
  <div class="illustration balloon" style="left:997px;top:10px;width:67px;height:124px" role="img" aria-label="Small striped hot air balloon"></div>
  <div class="illustration ferris-wheel" style="left:1033px;top:72px;width:167px;height:310px" role="img" aria-label="White ferris wheel"></div>

  <svg class="bands" width="1200" height="929" viewBox="0 0 1200 929" aria-hidden="true">
    <path class="band-sky" d="M-50,333 A105,80 0 0 1 160,333 A105,80 0 0 1 370,333 A105,80 0 0 1 580,333 A105,80 0 0 1 790,333 A105,80 0 0 1 1000,333 A105,80 0 0 1 1210,333 V929 H-50 Z"/>
    <path class="band-grass" d="M-120,475 A105,80 0 0 1 90,475 A105,80 0 0 1 300,475 A105,80 0 0 1 510,475 A105,80 0 0 1 720,475 A105,80 0 0 1 930,475 A105,80 0 0 1 1140,475 A105,80 0 0 1 1350,475 V929 H-120 Z"/>
    <path class="band-blush" d="M-60,630 A105,75 0 0 1 150,630 A105,75 0 0 1 360,630 A105,75 0 0 1 570,630 A105,75 0 0 1 780,630 A105,75 0 0 1 990,630 A105,75 0 0 1 1200,630 A105,75 0 0 1 1410,630 V929 H-60 Z"/>
  </svg>

  <div class="illustration line-art" style="left:191px;top:310px;width:120px;height:100px" role="img" aria-label="White line drawing of a book"></div>
  <div class="illustration line-art" style="left:868px;top:279px;width:196px;height:155px" role="img" aria-label="White carousel horse with acrobat"></div>
  <div class="illustration line-art" style="left:57px;top:455px;width:336px;height:175px" role="img" aria-label="White line drawing of a bicycle"></div>
  <div class="illustration line-art" style="left:966px;top:460px;width:170px;height:118px" role="img" aria-label="White line drawing of a bow"></div>

  <svg class="type-layer" width="1200" height="929" viewBox="0 0 1200 929">
    <text class="headline" x="18" y="212" font-size="190" textLength="973" lengthAdjust="spacingAndGlyphs">SAVE 10%</text>
    <text class="script" x="356" y="382" font-size="95">books, toys,</text>
    <text class="script" x="439" y="553" font-size="100">&amp; clothes</text>
    <text class="headline" x="38" y="718" font-size="62" textLength="855" lengthAdjust="spacingAndGlyphs">WHEN YOU SHOP ONLINE</text>
    <text class="web-address" x="40" y="785" font-size="58" textLength="821" lengthAdjust="spacingAndGlyphs">www.littleplume.com.au</text>
    <text class="promo-code" x="42" y="847" font-size="35">use code 10promo at the check out</text>
    <text class="labels" x="42" y="917">
      <tspan class="light">Tavel K</tspan>
      <tspan class="dark" dx="14">Brindle</tspan>
      <tspan class="light" dx="14">Zorra</tspan>
      <tspan class="dark" dx="14">Pebble Creek Sandals</tspan>
      <tspan class="light" dx="14">Rovandi Kids</tspan>
      <tspan class="dark" dx="8">and many more</tspan>
    </text>
    <circle class="brand-dot" cx="1043" cy="710" r="42"/>
    <text class="brand-name" x="1043" y="795" font-size="30" text-anchor="middle">Little Plume</text>
  </svg>
</main>
</body>
</html>
```